Company Gift Card Designs

I would like to have 2 gift cards designed.

Both cards need to be in our company colors and have a non-white background. Both will need to follow the attached spec sheet from the card vendor.

Card 1 - will need to have the words Thank you on the card and use the KTB Logo

Card 2 - will need to have both the KTB logo and the Zel480 Logo incorporated into the design.

```html
<!DOCTYPE html>
<html lang="en">
<head>
<meta charset="utf-8">
<title>KTB Gift Cards</title>
<link rel="stylesheet" href="https://fonts.googleapis.com/css2?family=Pinyon+Script&display=swap">
<style>
  :root {
    --page: #ffffff;
    --card: #111111;
    --card-edge: #191919;
    --ribbon: #e5231b;
    --ribbon-light: #f2332a;
    --ribbon-dark: #b8140f;
    --gold: #e8b65a;
    --white: #ffffff;
    --shadow: rgba(0, 0, 0, 0.35);
  }
  html, body {
    margin: 0;
    padding: 0;
    width: 974px;
    height: 1200px;
    overflow: hidden;
    background: var(--page);
  }
  .canvas {
    position: relative;
    width: 974px;
    height: 1200px;
  }
  .gift-card {
    position: absolute;
    left: 87px;
    width: 800px;
    height: 510px;
    border-radius: 34px;
    background: radial-gradient(ellipse at 80% 20%, var(--card-edge), var(--card) 60%);
    box-shadow: 0 8px 14px var(--shadow);
    overflow: hidden;
  }
  .gift-card--thanks { top: 60px; }
  .gift-card--partners { top: 630px; }

  .ribbon-band {
    position: absolute;
  }
  .ribbon-band--vertical {
    left: 140px;
    top: 0;
    width: 34px;
    height: 100%;
    background: linear-gradient(90deg, var(--ribbon-dark), var(--ribbon-light) 45%, var(--ribbon) 100%);
  }
  .ribbon-band--horizontal {
    left: 0;
    top: 72px;
    width: 100%;
    height: 33px;
    background: linear-gradient(180deg, var(--ribbon-light), var(--ribbon) 50%, var(--ribbon-dark));
  }
  .ribbon-bow {
    position: absolute;
    left: 72px;
    top: 30px;
    width: 170px;
    height: 120px;
    border-radius: 14px;
    background: linear-gradient(180deg, var(--ribbon-light), var(--ribbon) 55%, var(--ribbon-dark));
  }

  .greeting {
    position: absolute;
    margin: 0;
    font-family: "Pinyon Script", cursive;
    font-weight: 400;
    line-height: 1;
    white-space: nowrap;
  }
  .greeting-thank { color: var(--gold); }
  .greeting-you { color: var(--white); }
  .gift-card--thanks .greeting-thank { left: 212px; top: 147px; font-size: 210px; }
  .gift-card--thanks .greeting-you { left: 386px; top: 251px; font-size: 170px; }
  .gift-card--partners .greeting-thank { left: 279px; top: 126px; font-size: 184px; }
  .gift-card--partners .greeting-you { left: 431px; top: 220px; font-size: 152px; }

  .brand-mark {
    position: absolute;
    display: flex;
    align-items: center;
    gap: 16px;
    font-family: "Pinyon Script", cursive;
    font-weight: 400;
    color: var(--white);
    font-size: 52px;
    line-height: 1;
    white-space: nowrap;
  }
  .brand-divider {
    width: 2px;
    height: 42px;
    background: var(--white);
  }
  .gift-card--thanks .brand-mark { right: 68px; bottom: 38px; }
  .gift-card--partners .brand-mark { right: 76px; bottom: 38px; }
</style>
</head>
<body>
<main class="canvas">
  <section class="gift-card gift-card--thanks" aria-label="KTB thank you gift card">
    <div class="ribbon-band ribbon-band--horizontal"></div>
    <div class="ribbon-band ribbon-band--vertical"></div>
    <div class="ribbon-bow" role="img" aria-label="Red satin gift bow tied where the ribbons cross"></div>
    <p class="greeting greeting-thank">Thank</p>
    <p class="greeting greeting-you">you</p>
    <div class="brand-mark"><span class="brand-name">KTB</span></div>
  </section>

  <section class="gift-card gift-card--partners" aria-label="KTB and Zel480 thank you gift card">
    <div class="ribbon-band ribbon-band--horizontal"></div>
    <div class="ribbon-band ribbon-band--vertical"></div>
    <div class="ribbon-bow" role="img" aria-label="Red satin gift bow tied where the ribbons cross"></div>
    <p class="greeting greeting-thank">Thank</p>
    <p class="greeting greeting-you">you</p>
    <div class="brand-mark">
      <span class="brand-name">KTB</span>
      <span class="brand-divider"></span>
      <span class="brand-name">Zel480</span>
    </div>
  </section>
</main>
</body>
</html>
```